Super Greens Label for Supplement Bottle

We want to design a front label for a health supplement bottle. The product is called Leafy Blendbite Chews™. This will be a new product so there is no current website for the product. The focus is on supergreens that taste great and deliver support for energy, digestion, and immune defense.
We want it to be modern, vibrant and appealing.
Bottle size: standard size supplement CLEAR bottle size, with white child resistant cap and the label panel dimensions are 3” x 7”. The label should be primarily white and green, with a touch of red; (see color palettes)/it can also ONLY be white and green. See samples attached.
We are only focused on the front of the bottle design, not on the back, but leave space for the supplement panel and other text on the back.
So the text for the front of the bottle is:
RT Dalloway's
Leafy Blendbite Chews™
Super Greens Blend for:
Energy, Digestion, and Immune Support*
60 Gummies | Dietary Supplement
Raspberry Flavor Gummies
Off to side of the label:
Non-GMO
Vegan Friendly
Plant-Based
Gelatin Free
Colors
Designer to choose colors to be used in the design.
Look and feel
Each slider illustrates characteristics of the customer's brand and the style your logo design should communicate.

```html
<!DOCTYPE html>
<html lang="en">
<head>
<meta charset="utf-8">
<title>Leafy Blendbite Chews – Front Label</title>
<link href="https://fonts.googleapis.com/css2?family=Quicksand:wght@500;600;700&display=swap" rel="stylesheet">
<style>
  :root {
    --green-deep: #0f763d;
    --green-dark: #0a5e32;
    --green-lime: #8db43a;
    --green-glow: #9dbb3a;
    --berry-red: #d3202e;
    --white: #ffffff;
    --page: #ffffff;
  }
  * { box-sizing: border-box; margin: 0; padding: 0; }
  html, body { width: 1200px; height: 1000px; overflow: hidden; background: var(--page); }
  body { position: relative; font-family: "Quicksand", sans-serif; color: var(--white); }

  .label {
    position: absolute; left: 76px; top: 275px;
    width: 1048px; height: 449px;
    background: var(--green-deep);
    overflow: hidden;
  }

  /* front panel */
  .front-panel {
    position: absolute; left: 0; top: 0; width: 438px; height: 100%;
    background: radial-gradient(ellipse 70% 75% at 40% 100%, var(--green-glow) 0%, #4f9a3a 45%, var(--green-deep) 85%);
    text-align: center;
  }
  .tagline {
    position: absolute; left: 0; width: 100%; top: 42px;
    font-size: 14.5px; font-weight: 500; line-height: 19px;
  }
  .product-name {
    position: absolute; left: 0; width: 100%; top: 94px;
    font-weight: 700; line-height: 1;
  }
  .product-name .line-one { display: block; font-size: 40px; letter-spacing: -0.5px; }
  .product-name .line-two { display: block; font-size: 60px; margin-top: 4px; letter-spacing: -0.5px; }

  .count-badge {
    position: absolute; left: 96px; top: 207px; width: 82px; height: 82px;
    border-radius: 50%; background: var(--green-dark);
    font-size: 38px; font-weight: 700; line-height: 82px; text-align: center;
  }
  .count-text { position: absolute; left: 183px; top: 222px; text-align: left; }
  .count-text .count-unit { display: block; font-size: 25px; font-weight: 700; line-height: 26px; }
  .count-text .count-type { display: block; font-size: 14.5px; font-weight: 600; line-height: 18px; }

  .fruit-art {
    position: absolute; left: 132px; top: 290px; width: 205px; height: 108px;
    border-radius: 50% 50% 40% 40%;
    background: radial-gradient(ellipse at 55% 55%, #e0283f 0%, #c41e36 55%, rgba(90,140,60,0.6) 85%, rgba(90,140,60,0) 100%);
  }
  .flavor-pill {
    position: absolute; left: 146px; top: 392px; width: 165px; height: 35px;
    border-radius: 18px; background: var(--berry-red);
    font-size: 15px; font-weight: 700; line-height: 35px; text-align: center;
  }

  /* claims strip */
  .claims-strip {
    position: absolute; left: 438px; top: 0; width: 145px; height: 100%;
    background: linear-gradient(180deg, var(--green-lime) 0%, #5f9a3c 40%, #2a8240 75%, var(--green-deep) 100%);
    box-shadow: -6px 0 10px rgba(0,0,0,0.25), 6px 0 10px rgba(0,0,0,0.2);
    text-align: center;
  }
  .claim { position: absolute; left: 0; width: 100%; }
  .claim svg { display: block; margin: 0 auto; }
  .claim-label { display: block; font-size: 11.5px; font-weight: 600; letter-spacing: 0.2px; margin-top: 14px; }
  .claim-gmo { top: 40px; }
  .claim-vegan { top: 132px; }
  .claim-plant { top: 238px; }
  .claim-gelatin { top: 332px; }

  /* back area left open for supplement facts */
  .back-panel { position: absolute; left: 583px; top: 0; right: 0; height: 100%; background: var(--green-deep); }
</style>
</head>
<body>
  <div class="label">
    <section class="front-panel">
      <p class="tagline">Super Greens Blend for:<br>Energy, Digestion, Immune Support</p>
      <h1 class="product-name">
        <span class="line-one">Leafy Blendbite</span>
        <span class="line-two">Chews</span>
      </h1>
      <div class="count-badge">60</div>
      <p class="count-text">
        <span class="count-unit">Gummies</span>
        <span class="count-type">| Dietary Supplement</span>
      </p>
      <div class="fruit-art" role="img" aria-label="Cluster of fresh red raspberries with green leaves"></div>
      <div class="flavor-pill">Raspberry Flavor</div>
    </section>

    <aside class="claims-strip">
      <div class="claim claim-gmo">
        <svg width="48" height="48" viewBox="0 0 48 48" fill="none" stroke="#fff" stroke-width="3" stroke-linecap="round">
          <circle cx="24" cy="24" r="21"/>
          <line x1="9" y1="9" x2="39" y2="39"/>
          <path d="M18 10 C30 18 18 30 30 38" stroke-width="2.5"/>
          <path d="M30 10 C18 18 30 30 18 38" stroke-width="2.5"/>
          <line x1="20" y1="16" x2="28" y2="16" stroke-width="2"/>
          <line x1="20" y1="32" x2="28" y2="32" stroke-width="2"/>
        </svg>
        <span class="claim-label">NON GMO</span>
      </div>
      <div class="claim claim-vegan">
        <svg width="52" height="48" viewBox="0 0 52 48" fill="#fff">
          <path d="M8 14 L16 14 L22 36 L28 14 L33 14 L25 46 L18 46 Z"/>
          <path d="M31 20 C31 8 40 2 50 2 C50 14 42 20 31 20 Z"/>
        </svg>
        <span class="claim-label">VEGAN FRIENDLY</span>
      </div>
      <div class="claim claim-plant">
        <svg width="60" height="42" viewBox="0 0 60 42" fill="#fff">
          <path d="M28 22 C20 22 4 18 2 6 C16 6 26 12 28 22 Z"/>
          <path d="M30 20 C32 8 44 2 58 2 C56 16 42 22 30 20 Z"/>
          <path d="M29 20 C28 28 26 35 22 41" stroke="#fff" stroke-width="2" fill="none"/>
        </svg>
        <span class="claim-label">PLANT BASED</span>
      </div>
      <div class="claim claim-gelatin">
        <svg width="48" height="48" viewBox="0 0 48 48" fill="none" stroke="#fff" stroke-width="3" stroke-linejoin="round">
          <path d="M8 34 L10 12 C10 6 38 6 38 12 L40 34 Z"/>
          <line x1="18" y1="12" x2="17" y2="34"/>
          <line x1="30" y1="12" x2="31" y2="34"/>
          <line x1="4" y1="40" x2="44" y2="40"/>
          <line x1="24" y1="34" x2="24" y2="40"/>
        </svg>
        <span class="claim-label">GELATIN FREE</span>
      </div>
    </aside>

    <div class="back-panel"></div>
  </div>
</body>
</html>
```